4.25" x 11" Door Hanger Design - Cable Quick Internet Service

We are sourcing a door hanger that will be used to micro target specific neighborhoods with our new "Cable Quick" internet service offering

This will be used as a template for a new type of plan we are offering in very specific areas. The first will be "Willow Hollow" with 3 plan offerings.

Stock photos should be family friendly but we want something modern and exciting that we can use to advertise a new internet service offering.
Updates

Sorry if I missed this before, but we would of course like our website and phone number with an encouragement to call us Website: www.brandovex.example Phone: 555-203-4187

Target Market(s)

Residential Internet Service

Industry/Entity Type

Internet Service Provider

Font styles to use
Sans Serif
Other font styles liked:
• RockoFLF

Colors

Designer to choose colors to be used in the design.

Requirements
Must have
• 1) Our logo with "Internet Services" nearby to show "Brandovex Internet Services" (name and what we do)
• 2) "Cable Quick Internet Service is Now Available in Willow Hollow!"
• 3) Show three plans, we don't know the price yet and we will edit the winning design eventually when we know the exact price.
• 100 Mbps $XX.XX per month
• 250 Mbps $XX.XX per month
• 1 Gbps $XX.XX per month
• 4) The plan names and prices should be easy to edit in the future if/when we try these in different markets.
• This ad will be modified with specific information like prices and the location when we use it in specific spots.
• We will be using Quikprintova for the printing, please use their website for the punch hole location, dimensions, etc.
• https://www.quikprintova.example/door-hanger-printing/
Nice to have
• We want to demonstrate far higher than normal internet service speed offerings. This can use whatever you think demonstrates this idea to the customers better, something like a speed test looking logo
Should not have
• Do not copy our website, we want a fresh design

```html
<!DOCTYPE html>
<html lang="en">
<head>
<meta charset="utf-8">
<title>Brandovex Internet Services – Door Hanger</title>
<link href="https://fonts.googleapis.com/css2?family=Raleway:wght@300;400;500;600;700&family=Poppins:wght@600;700&display=swap" rel="stylesheet">
<style>
  :root {
    --purple: #3d2a78;
    --purple-dark: #2c2462;
    --sky: #8dbbf0;
    --orange: #ef6b2a;
    --brand-blue: #3a8fd8;
    --white: #ffffff;
  }
  html, body {
    margin: 0;
    padding: 0;
    width: 1200px;
    height: 3103px;
    overflow: hidden;
    background: var(--white);
  }
  .door-hanger {
    position: relative;
    width: 1200px;
    height: 3103px;
    overflow: hidden;
    background: var(--white);
    font-family: "Raleway", sans-serif;
  }
  .backdrop {
    position: absolute;
    inset: 0;
  }
  .brand-header {
    position: absolute;
    top: 740px;
    left: 0;
    width: 1200px;
    text-align: center;
    color: var(--white);
  }
  .brand-name {
    display: inline-flex;
    align-items: center;
    gap: 26px;
    font-family: "Raleway", sans-serif;
    font-weight: 400;
    font-size: 128px;
    line-height: 1;
    letter-spacing: -1px;
  }
  .brand-dot {
    width: 44px;
    height: 44px;
    border-radius: 50%;
    background: var(--white);
  }
  .brand-tagline {
    margin-top: 54px;
    font-weight: 400;
    font-size: 33px;
    letter-spacing: 15px;
    padding-left: 15px;
  }
  .headline {
    position: absolute;
    top: 1012px;
    left: 0;
    width: 1200px;
    margin: 0;
    text-align: center;
    font-family: "Raleway", sans-serif;
    font-weight: 600;
    font-size: 60px;
    line-height: 76px;
    color: var(--sky);
  }
  .headline .location {
    font-family: "Poppins", sans-serif;
    font-weight: 700;
    color: var(--white);
  }
  .hero-photo {
    position: absolute;
    left: 207px;
    top: 1227px;
    width: 786px;
    height: 786px;
    border-radius: 50%;
    background: radial-gradient(circle at 50% 45%, #ffffff 0%, #f3f5f9 45%, #ffffff 70%);
    overflow: hidden;
  }
  .hero-photo .cable {
    position: absolute;
    left: 120px;
    top: 200px;
    width: 560px;
    height: 200px;
    border-radius: 100px;
    background: linear-gradient(100deg, #d9dde4 0%, #6f9ee6 35%, #2d63d2 70%, #1e49b0 100%);
    opacity: 0.85;
  }
  .plan {
    position: absolute;
    left: 248px;
    width: 760px;
    height: 270px;
  }
  .plan-bar {
    position: absolute;
    left: 0;
    top: 78px;
    width: 560px;
    height: 118px;
    border-radius: 22px 0 0 22px;
    background: var(--purple);
    box-shadow: 6px 10px 12px rgba(0,0,0,0.28);
    color: var(--white);
    font-family: "Poppins", sans-serif;
    font-weight: 600;
    font-size: 56px;
    line-height: 118px;
    padding-left: 64px;
    box-sizing: border-box;
  }
  .plan-price {
    position: absolute;
    left: 490px;
    top: 8px;
    width: 256px;
    height: 256px;
    border-radius: 50%;
    background: var(--orange);
    box-shadow: 6px 10px 14px rgba(0,0,0,0.3);
    color: var(--white);
    font-family: "Raleway", sans-serif;
    text-align: center;
  }
  .plan-price .currency {
    position: absolute;
    left: 34px;
    top: 48px;
    font-weight: 700;
    font-size: 54px;
  }
  .plan-price .amount {
    position: absolute;
    left: 0;
    right: 0;
    top: 52px;
    font-weight: 600;
    font-size: 116px;
    line-height: 1;
    padding-left: 28px;
  }
  .plan-price .term {
    position: absolute;
    left: 0;
    right: 0;
    top: 172px;
    font-family: "Poppins", sans-serif;
    font-weight: 600;
    font-size: 25px;
    padding-left: 20px;
  }
  .plan--100 { top: 1920px; }
  .plan--250 { top: 2265px; }
  .plan--1000 { top: 2610px; }
  .footer-brand {
    position: absolute;
    left: 72px;
    top: 2904px;
    display: flex;
    align-items: center;
    gap: 16px;
    font-family: "Raleway", sans-serif;
    font-weight: 400;
    font-size: 80px;
    line-height: 1;
    color: var(--brand-blue);
  }
  .footer-brand .brand-dot {
    width: 28px;
    height: 28px;
    background: var(--brand-blue);
  }
</style>
</head>
<body>
<main class="door-hanger">
  <svg class="backdrop" width="1200" height="3103" viewBox="0 0 1200 3103" aria-hidden="true">
    <polygon points="0,0 1200,0 1200,1520 0,1790" fill="var(--purple)"/>
    <circle cx="600" cy="1620" r="393" fill="var(--white)"/>
    <circle cx="161" cy="1908" r="103" fill="var(--purple-dark)"/>
    <circle cx="300" cy="1804" r="58" fill="var(--purple-dark)"/>
  </svg>

  <div class="hero-photo" role="img" aria-label="Photo of a blue network cable with its connector plug on a white background">
    <div class="cable"></div>
  </div>

  <header class="brand-header">
    <div class="brand-name"><span class="brand-dot"></span>Brandovex</div>
    <div class="brand-tagline">INTERNET SERVICES</div>
  </header>

  <h1 class="headline">Cable Quick Internet Service is Now<br>Available in <span class="location">Willow Hollow!</span></h1>

  <section class="plan plan--100">
    <div class="plan-bar">- 100 Mbps</div>
    <div class="plan-price"><span class="currency">$</span><span class="amount">XX</span><span class="term">per month</span></div>
  </section>

  <section class="plan plan--250">
    <div class="plan-bar" style="padding-left:50px">- 250 Mbps</div>
    <div class="plan-price"><span class="currency">$</span><span class="amount">XX</span><span class="term">per month</span></div>
  </section>

  <section class="plan plan--1000">
    <div class="plan-bar">- 1 Gbps</div>
    <div class="plan-price"><span class="currency">$</span><span class="amount">XX</span><span class="term">per month</span></div>
  </section>

  <footer class="footer-brand"><span class="brand-dot"></span>Brandovex</footer>
</main>
</body>
</html>
```